Redesign criminal justice consulting website

We run a small professional services firm that does research, evaluation, consulting, and training on criminal justice issues. We need to redesign our website (www.brvolquest.com). The existing site is something we made ourselves. It is unprofessional and does not do a good job of communicating what we do or who we are.

We would like the new site to provide a basic overview of what we do. Moreover, we would like it to communicate several themes that represent who we are:

* global

* innovative

* analytical

* practical

We view the principal design challenge as figuring out a subtle, interesting, and graphically appealing way to communicate these themes.

Target Market(s)

Our primary customers are governments, research firms, criminal justice agencies, and schools. The people who we want to find our site are seeking research, evaluation, training, or consulting services related to crime, criminal justice, or policing.

Industry/Entity Type

Consulting

Number of Pages Required

2 pages

Requirements
Must have
• 1. We would like the site to use our logo. It is attached (please use the maroon 4-color version with the company name but without the slogan). The site should also use the colors present in our logo. It may use other colors as well, as long as these colors coordinate with the logo colors.

• 2. For main pages or buttons, we need the following:
• *Home
• *About BVQ
• *Services
• *E-Training
• *Resources
• *Contact BVQ

• 3. We like simple, crisp, subtle designs over "busier," cluttered, or very complex designs.

• 4. We'd like to receive, at a minimum, the home page and a sample inner page.
Nice to have
• We need some help in thinking through what regions or sections should exist on the home page. We are thinking about having a window on there where we can make announcements about recent developments like new reports, new e-training videos, new photographs, etc... We are open to suggestions here.
Should not have
• 1. Gimmicky or overused clipart.
• 2. Cliched images associated with criminal justice, including magnifying glasses, scales of justice, etc... Our logo makes a subtle nod to criminal justice through the use of a fingerprint as the dot on the "J" in the company initials. That''s sufficient for our purposes. Concentrate instead on the themes listed above.
• 3. Major use of colors that don't match our logo, like blue.

```html
<!DOCTYPE html>
<html lang="en">
<head>
<meta charset="utf-8">
<title>BVQ – Brvol Quest Analysts</title>
<link rel="stylesheet" href="https://fonts.googleapis.com/css2?family=Arimo:wght@400;700&family=Didact+Gothic&family=Sorts+Mill+Goudy&display=swap">
<style>
:root{
  --maroon:#8e2326;
  --maroon-dark:#7a1c1f;
  --maroon-light:#b4474a;
  --link:#c0393c;
  --pink-wash:#f7e6e7;
  --side-bg:#fbf3f3;
  --text:#111;
  --text-soft:#333;
  --white:#fff;
}
*{margin:0;padding:0;box-sizing:border-box}
html,body{width:1200px;height:2262px;overflow:hidden;background:var(--white)}
body{font-family:"Arimo",Arial,sans-serif;color:var(--text);position:relative}
a{color:var(--link);text-decoration:none}

.page{position:absolute;left:0;width:1200px}
.page--home{top:0;height:1158px}
.page--about{top:1200px;height:1062px}

/* header */
.site-header{position:absolute;left:0;top:0;width:1200px;height:154px;
  background:linear-gradient(180deg,#fff 0%,#fdf7f7 60%,#f4e1e2 100%)}
.header-globe{position:absolute;right:0;top:0;width:330px;height:154px;
  background:radial-gradient(ellipse at 65% 55%,#f0d2d4 0%,#f6e4e5 45%,rgba(255,255,255,0) 75%)}
.brand{position:absolute;left:32px;top:28px;display:flex;align-items:center;gap:14px}
.brand-mark{width:22px;height:22px;border-radius:50%;background:var(--maroon)}
.brand-name{font-family:"Sorts Mill Goudy",Georgia,serif;color:var(--maroon);font-size:46px;line-height:1}
.brand-name small{font-size:26px;letter-spacing:2px}

/* nav */
.main-nav{position:absolute;left:0;top:154px;width:1200px;height:42px;
  background:linear-gradient(180deg,var(--maroon-light) 0%,var(--maroon) 55%,var(--maroon-dark) 100%)}
.main-nav a{position:absolute;top:0;height:42px;line-height:42px;color:var(--white);font-size:20px;width:146px}
.main-nav a.is-active{background:#c5686a}

/* hero */
.hero-photo{position:absolute;left:0;top:196px;width:1200px;height:346px;
  background:linear-gradient(90deg,#d7c7bd 0%,#efe9e4 30%,#cfc5b8 55%,#8b7460 72%,#e6e0da 100%)}

/* home content */
.announcements{position:absolute;left:0;top:542px;width:330px;height:578px;background:var(--side-bg);
  border-right:2px solid #f3e3e3;padding:24px 32px 0 32px;font-size:16.5px;line-height:21.5px}
.announcements h2{color:var(--maroon);font-size:19px;font-weight:700;margin-bottom:24px}
.news-item{margin-bottom:24px}
.news-item time{display:block;font-weight:700;margin-bottom:1px}
.intro{position:absolute;left:355px;top:542px;width:830px;padding-top:14px;font-size:19.5px;line-height:24px}
.intro h1{font-family:"Sorts Mill Goudy",Georgia,serif;font-weight:400;color:var(--maroon);font-size:32px;line-height:1.2;margin-bottom:32px}
.intro p{margin-bottom:24px}

/* footer */
.site-footer{position:absolute;left:0;width:1200px;height:38px;background:var(--maroon);color:var(--white);
  font-size:14.5px;display:flex;align-items:center;justify-content:space-between;padding:0 27px 0 32px}
.site-footer a{color:var(--white)}
.site-footer .sep{margin:0 8px}
.page--home .site-footer{top:1120px}
.page--about .site-footer{top:1022px;height:40px}

/* about content */
.about-intro{position:absolute;left:0;top:246px;width:342px;text-align:right;font-family:"Sorts Mill Goudy",Georgia,serif}
.about-intro h1{font-weight:400;color:var(--maroon);font-size:37px;line-height:1;margin-right:14px;margin-bottom:20px}
.about-intro p{font-size:23px;line-height:27.5px;color:var(--text-soft)}
.team-photo{position:absolute;left:42px;top:558px;width:300px;height:200px;
  background:linear-gradient(90deg,#3a2a24 0%,#c9b6a8 35%,#efe8e2 65%,#5a4a44 100%)}
.principles{position:absolute;left:387px;top:258px;width:770px;font-family:"Didact Gothic","Century Gothic",sans-serif;color:var(--text-soft);font-size:17px;line-height:21px}
.principles h2{font-weight:400;color:var(--maroon);font-size:17.5px;letter-spacing:.5px;text-transform:uppercase;margin-bottom:20px}
.principles section{margin-bottom:47px}
.principles p + p{margin-top:20px}
</style>
</head>
<body>

<div class="page page--home">
  <header class="site-header">
    <div class="header-globe" role="img" aria-label="Faint globe showing the Americas"></div>
    <div class="brand">
      <span class="brand-mark"></span>
      <span class="brand-name">BVQ <small>BRVOL QUEST ANALYSTS</small></span>
    </div>
  </header>
  <nav class="main-nav">
    <a class="is-active" style="left:0;padding-left:42px" href="#">Home</a>
    <a style="left:186px;padding-left:23px" href="#">About BVQ</a>
    <a style="left:400px;padding-left:22px" href="#">Services</a>
    <a style="left:594px;padding-left:22px" href="#">E-Training</a>
    <a style="left:802px;padding-left:22px" href="#">Resources</a>
    <a style="left:1016px;padding-left:22px;width:184px" href="#">Contact BVQ</a>
  </nav>
  <div class="hero-photo" role="img" aria-label="Photo of a team of professionals discussing around a table"></div>

  <aside class="announcements">
    <h2>Announcements</h2>
    <div class="news-item"><time>15 Dec 2009</time>New E-Training <a href="#">Sample E-training Title</a> is available now.</div>
    <div class="news-item"><time>13 Dec 2009</time><a href="#">Sample Report</a> about luctus, mi eget tristique lacinia, nulla orci sagittis ante.</div>
    <div class="news-item"><time>12 Dec 2009</time>Suspendisse ac felis. Nunc a lectus. Suspendisse potenti. Donec cursus <a href="#">lectus ac nisl</a>.</div>
    <div class="news-item"><time>10 Dec 2009</time>Aliquam sodales. Curabitur pellen-tesque.</div>
    <div class="news-item"><time>8 Dec 2009</time>Morbi id massa in <a href="#">ligula feugiat</a> egestas. Ac ante sodales sagittis.</div>
  </aside>

  <main class="intro">
    <h1>Innovation in crime prevention</h1>
    <p>Brvol Quest Analysts are a consulting firm based in Northern Virginia near Washington, DC. We specialize in providing training, technical assistance, research, evaluation and other services related to crime prevention and criminal justice.</p>
    <p>Our services are provided by a network of experts with a variety of backgrounds in social science, law enforcement, criminal law, forensics, and other professions. Projects range in scope from brief consultations, reports, or training sessions to comprehensive, multi-year system-wide transformation efforts.</p>
    <p>Our clients include governments, public agencies, professional associations, universities and research centers, non-governmental organizations, and professional services firms. We also have significant international experience and have worked in both developed and developing nations.</p>
    <p>We specialize in working closely with our clients to design tailored, innovative solutions. Call today and explore how we can be of service.</p>
  </main>

  <footer class="site-footer">
    <div><a href="#">Home</a><span class="sep">|</span><a href="#">Sitemap</a><span class="sep">|</span><a href="#">Contact BVQ</a></div>
    <div>Copyright 2009, Brvol Quest Analysts, Inc. All Rights Reserved.</div>
  </footer>
</div>

<div class="page page--about">
  <header class="site-header">
    <div class="header-globe" role="img" aria-label="Faint globe showing the Americas"></div>
    <div class="brand">
      <span class="brand-mark"></span>
      <span class="brand-name">BVQ <small>BRVOL QUEST ANALYSTS</small></span>
    </div>
  </header>
  <nav class="main-nav">
    <a style="left:0;padding-left:42px" href="#">Home</a>
    <a class="is-active" style="left:186px;padding-left:23px" href="#">About BVQ</a>
    <a style="left:400px;padding-left:22px" href="#">Services</a>
    <a style="left:594px;padding-left:22px" href="#">E-Training</a>
    <a style="left:802px;padding-left:22px" href="#">Resources</a>
    <a style="left:1016px;padding-left:22px;width:184px" href="#">Contact BVQ</a>
  </nav>

  <div class="about-intro">
    <h1>About BVQ</h1>
    <p>BVQ operates on a set of core<br>principles that influence<br>everything we do.</p>
  </div>
  <div class="team-photo" role="img" aria-label="Photo of a smiling group of colleagues"></div>

  <main class="principles">
    <section>
      <h2>Analysis</h2>
      <p>Meaningful analysis is what we believe in and what we do best. Analysis is vital for planning successful change efforts in organizations. Knee-jerk change efforts that result from faulty impressions or incorrect assumptions often fail. Questioning routine practices, while often controversial, is essential.</p>
    </section>
    <section>
      <h2>Inclusiveness</h2>
      <p>History teaches us that change efforts that exclude internal and external stakeholders are unlikely to succeed.</p>
    </section>
    <section>
      <h2>Tailoring and Customization</h2>
      <p>The most effective innovations are those that are tailored or customized to the specific and unique characteristics of each problem. Copying innovations from other jurisdictions is often ineffective and sometimes even counterproductive.</p>
    </section>
    <section>
      <h2>Evaluation and Assessment</h2>
      <p>Implementing effective change means evaluating and assessing the change effort at every stage, generating feedback from employees, clients, and other stakeholders, and then adapting as necessary.</p>
      <p>As external consultants, we seek to learn about our clients: their worldview, their environment, their frustrations and accomplishments, their sources of embarrasment and their sources of pride. We work with them as partners at every step in the process. Avoid at all costs any consultant who makes recommendations about your organization without taking the time to learn about it first!</p>
    </section>
  </main>

  <footer class="site-footer">
    <div><a href="#">Home</a><span class="sep">|</span><a href="#">Sitemap</a><span class="sep">|</span><a href="#">Contact BVQ</a></div>
    <div>Copyright 2009, Brvol Quest Analysts, Inc. All Rights Reserved.</div>
  </footer>
</div>

</body>
</html>
```